varluso.net

We are a IT Service for the valley. I want a clean website, with new Design, like animated pictures. We focus on IT. Give me your best design. What I'm looking for is eye catching. Works with Smart Phones, and Quilo, Tab. Need a section for Submit a support tickets and Remote support. I'm looking for new ideals. I'm open mind, let me see what you guys can do.

Target Market(s)

My clients to see what service and products we have.

Industry/Entity Type

It Service

Requirements
Must have
• Able to submit a trouble tickets and works with Smart Phones, Quilo, Tab.

```html
<!DOCTYPE html>
<html lang="en">
<head>
<meta charset="utf-8">
<title>Varluso Technology</title>
<link rel="stylesheet" href="https://fonts.googleapis.com/css2?family=Open+Sans:wght@400;700;800&display=swap">
<style>
  :root {
    --navy: #2b3856;
    --red: #e3202a;
    --red-light: #f0525a;
    --red-dark: #c9161f;
    --text-dark: #111111;
    --text-body: #333333;
    --nav-text: #666666;
    --nav-top: #ffffff;
    --nav-bottom: #e9e9e9;
    --divider: #dcdcdc;
    --hero-top: #c9c9cc;
    --hero-bottom: #f1f1f2;
    --icon-top: #d9d9d9;
    --icon-bottom: #9a9a9a;
    --page: #ffffff;
  }
  * { box-sizing: border-box; margin: 0; padding: 0; }
  html, body {
    width: 1200px;
    height: 517px;
    overflow: hidden;
    background: var(--page);
    font-family: "Open Sans", Arial, sans-serif;
  }
  .page { position: relative; width: 1200px; height: 517px; }

  .brand {
    position: absolute;
    left: 170px;
    top: 26px;
    color: var(--navy);
    font-weight: 700;
    line-height: 1;
  }
  .brand-name { display: block; font-size: 62px; letter-spacing: -1px; }
  .brand-sub { display: block; font-size: 22px; letter-spacing: 13px; margin-top: 10px; padding-left: 2px; }

  .social {
    position: absolute;
    left: 937px;
    top: 100px;
    display: flex;
    gap: 5px;
    list-style: none;
  }
  .social-item {
    width: 27px;
    height: 27px;
    border-radius: 4px;
    background: linear-gradient(var(--icon-top), var(--icon-bottom));
    border: 1px solid #8a8a8a;
  }

  .main-nav {
    position: absolute;
    left: 158px;
    top: 140px;
    width: 889px;
    height: 41px;
    display: flex;
    border-radius: 7px;
    background: linear-gradient(var(--nav-top), var(--nav-bottom));
    box-shadow: 0 1px 3px rgba(0,0,0,0.35);
    overflow: hidden;
    list-style: none;
  }
  .nav-item {
    display: flex;
    align-items: center;
    justify-content: center;
    font-size: 13px;
    color: var(--nav-text);
    text-transform: uppercase;
    border-left: 1px solid var(--divider);
  }
  .nav-item:first-child { border-left: none; }
  .nav-item.is-active {
    color: #fff;
    background: linear-gradient(var(--red-light), var(--red) 50%, var(--red-dark));
  }
  .nav-home { width: 148px; }
  .nav-about { width: 153px; }
  .nav-repairs { width: 240px; }
  .nav-trade { width: 177px; }
  .nav-contact { flex: 1; }

  .hero {
    position: absolute;
    left: 159px;
    top: 200px;
    width: 887px;
    height: 330px;
    border: 2px solid #f0f0f0;
    border-radius: 4px;
    background: linear-gradient(var(--hero-top), var(--hero-bottom));
  }
  .hero-title {
    position: absolute;
    left: 40px;
    top: 130px;
    font-size: 37px;
    font-weight: 800;
    color: var(--text-dark);
    letter-spacing: -0.3px;
  }
  .hero-text {
    position: absolute;
    left: 41px;
    top: 181px;
    width: 290px;
    font-size: 15px;
    line-height: 20px;
    color: var(--text-body);
  }
  .hero-button {
    position: absolute;
    left: 40px;
    top: 252px;
    width: 177px;
    height: 37px;
    display: flex;
    align-items: center;
    justify-content: center;
    border-radius: 4px;
    color: #fff;
    font-size: 15px;
    text-transform: uppercase;
    background: linear-gradient(var(--red-light), var(--red) 50%, var(--red-dark));
    box-shadow: 0 2px 3px rgba(0,0,0,0.3);
  }
  .hero-visual {
    position: absolute;
    left: 418px;
    top: 31px;
    width: 355px;
    height: 300px;
    border-radius: 24px 24px 0 0;
    background: linear-gradient(#3a3a3c, #1a1a1b 40%, #5c6a78);
  }
</style>
</head>
<body>
<div class="page">
  <header>
    <div class="brand">
      <span class="brand-name">VARLUSO</span>
      <span class="brand-sub">TECHNOLOGY</span>
    </div>
    <ul class="social" aria-label="Social links">
      <li class="social-item"></li>
      <li class="social-item"></li>
      <li class="social-item"></li>
    </ul>
    <ul class="main-nav">
      <li class="nav-item nav-home is-active">Home</li>
      <li class="nav-item nav-about">About</li>
      <li class="nav-item nav-repairs">Repairs &amp; Upgrades</li>
      <li class="nav-item nav-trade">Buy &amp; Sell</li>
      <li class="nav-item nav-contact">Contact</li>
    </ul>
  </header>
  <section class="hero">
    <h1 class="hero-title">WE CAN HELP!</h1>
    <p class="hero-text">Need help upgrading your software? Check out our computer section or contact us now to schedule a servicing</p>
    <div class="hero-button">Book Repair</div>
    <div class="hero-visual" role="img" aria-label="Three smartphones with cracked screens"></div>
  </section>
</div>
</body>
</html>
```